Letterhead

We would like to use the logo attached as a new letterhead. Our problem is that we think the dark blue background is too much. We'd like a sleek, professional letterhead, and we'd like at least five options to choose from. I've also uploaded our old letterhead for reference of the style we're going for.

```html
<!DOCTYPE html>
<html lang="en">
<head>
<meta charset="utf-8">
<title>Aldermark Strategies Letterhead</title>
<link href="https://fonts.googleapis.com/css2?family=Open+Sans:wght@400;600&family=Tinos&display=swap" rel="stylesheet">
<style>
  :root {
    --navy: #1d3150;
    --gold: #c9a764;
    --cream: #f6f1e8;
    --ink: #4a4a4a;
    --backdrop: #e4e4e4;
    --paper: #ffffff;
  }
  * { box-sizing: border-box; margin: 0; padding: 0; }
  html, body { width: 1200px; height: 960px; overflow: hidden; }
  body {
    background: var(--backdrop);
    font-family: "Open Sans", sans-serif;
    color: var(--ink);
  }
  .letterhead {
    position: absolute;
    left: 252px; top: 30px;
    width: 696px; height: 900px;
    background: var(--paper);
    box-shadow: 0 4px 18px rgba(0,0,0,.12);
    overflow: hidden;
  }
  .watermark {
    position: absolute;
    left: 300px; top: 170px;
    width: 280px; height: 280px;
    background: var(--cream);
    opacity: .8;
  }
  .brand {
    position: absolute;
    left: 52px; top: 78px;
    display: flex; align-items: center; gap: 14px;
  }
  .brand-square { width: 30px; height: 30px; background: var(--navy); }
  .brand-name {
    font-weight: 600; font-size: 22px; letter-spacing: 3px;
    color: var(--navy); text-transform: uppercase;
  }
  .contact {
    position: absolute;
    right: 52px; top: 62px;
    font-family: "Tinos", serif;
    font-size: 12.5px; line-height: 1.45;
    color: var(--navy); text-align: right;
  }
  .contact-line { display: flex; justify-content: flex-end; align-items: center; gap: 6px; }
  .contact-icon { width: 10px; height: 10px; fill: var(--gold); }
  .recipient {
    position: absolute; left: 52px; top: 200px;
    font-size: 12px; line-height: 1.45;
  }
  .recipient-name { font-size: 13px; letter-spacing: .5px; color: #3d3d3d; }
  .letter-body {
    position: relative; z-index: 1;
    position: absolute; left: 52px; top: 278px; width: 520px;
    font-size: 11.5px; line-height: 1.6;
  }
  .letter-body p { margin-bottom: 14px; }
  .closing {
    position: absolute; left: 52px; top: 712px;
    font-size: 12px;
  }
  .signature-mark {
    width: 90px; height: 30px; margin: 8px 0 4px;
    background: linear-gradient(90deg, rgba(29,49,80,.12), rgba(29,49,80,.04));
    border-radius: 4px;
  }
  .signer-name { font-size: 14px; }
  .corner-swoosh { position: absolute; right: 0; bottom: 0; }
</style>
</head>
<body>
  <main class="letterhead">
    <div class="watermark" aria-hidden="true"></div>

    <header>
      <div class="brand">
        <span class="brand-square"></span>
        <span class="brand-name">Aldermark Strategies</span>
      </div>
      <address class="contact">
        <div>218 Harbor Lane Suite 310</div>
        <div>Juneau, Alaska 99801</div>
        <div class="contact-line">907 555 0148
          <svg class="contact-icon" viewBox="0 0 10 10"><path d="M2 1l2 0 1 2-1 1a5 5 0 0 0 2 2l1-1 2 1 0 2c-4 1-8-3-7-7z"/></svg>
        </div>
        <div class="contact-line">hello@aldermarkgroup.com
          <svg class="contact-icon" viewBox="0 0 10 10"><rect x="0" y="2" width="10" height="7"/><path d="M0 2l5 4 5-4" stroke="#fff" stroke-width="1" fill="none"/></svg>
        </div>
      </address>
    </header>

    <section class="recipient">
      <div class="recipient-name">MAREN HOLLOWAY</div>
      <div>Chief Exective Officer</div>
      <div>City/State, Zip Code</div>
    </section>

    <section class="letter-body">
      <p>Proin gravida nibh vel velit auctor aliquet. Aenean sollicitudin, lorem quis bibendum auctor, nisi elit consequat ipsum, nec sagittis sem nibh id elit. Duis sed odio sit amet nibh vulputate cursus a sit amet mauris. Morbi accumsan ipsum velit. Nam nec tellus a odio tincidunt auctor a ornare odio. Sed non mauris vitae erat consequat auctor eu in elit. Class aptent taciti sociosqu ad litora torquent ugue. Sed non neque elit. Sed ut imperdiet nisi. Proin condimentum fermentum nunc. Etiam pharetra, imperdiet nisi. Proin condimentum fermentum nunc. Etiam pharetra, erat sed fermentum feugiat, velit mauris egestas quam, ut aliquam massa nisl quis neque. Suspendisse in orci enim.</p>
      <p>This is Photoshop's version of Lorem Ipsum. Proin gravida nibh vel velit auctor aliquet. Aenean sollicitudin, lorem quis bibendum auctor, nisi elit consequat ipsum, nec sagittis sem nibh id elit. Duis sed odio sit amet nibh vulputate cursus a sit amet mauris. Mo rbi accumsan ipsum velit. Nam nec tellus a odio tincidunt auctor a ornare odio. Sed non mauris vitae erat consequat auctor eu in elit. Class aptt consequat auctor eu in elit. Class aptent taciti sociosqu ad litora torquent per conubia nostra, per inceptos himenaeos. Mauris in erat justo.</p>
      <p>Nullam ac urna eu felis dapibus condimentum sit amet a augue. Sed non neque elit. Sed ut imperdiet nisi. Proin condimentum fermentum nunc. Etiam pharetra, erat sed fermentum feugiat, velit mauris egestas quam. Nullam ac urna eu felis dapibus condimentum sit amet a aug pharetra, erat sed fermentum feugiat, velit mauris egestas quam. Nullam ac urna eu felis dapibus condimentum sit amet a augue. Sed non neque elit. Sed ut imperdiet nisi. Proin condimentum fermentum nunc.</p>
    </section>

    <section class="closing">
      <div>Sincerely,</div>
      <div class="signature-mark" role="img" aria-label="Handwritten signature"></div>
      <div class="signer-name">Jonah Whitfield</div>
    </section>

    <svg class="corner-swoosh" width="300" height="360" viewBox="0 0 300 360" aria-hidden="true">
      <path d="M300 0 L300 360 L100 360 C170 255 245 135 300 0 Z" fill="var(--navy)"/>
      <path d="M296 12 C230 140 150 260 68 360 L88 360 C165 262 238 142 296 12 Z" fill="var(--gold)"/>
    </svg>
  </main>
</body>
</html>
```